Carpentry and Building Business Card

I'm looking for a business card that is minimalistic and that incorporates the theme of my Velmi logo.
On one side I'd like the VELMI logo with my details on the other side.
Double sided with curved edges

Target Market(s)

Construction / renovation
Adults

Industry/Entity Type

Tradesman

Contact Information for Business Card

Logo on one side, details on the other

Colors

Designer to choose only greyscale colors for use in the design.

Requirements
Must have
• Niko Barlettis
VELMI CONSTRUCT
Carpentry & Building Services
0412385726
Velmiconstruct@brindlemail.com
Lic No. 618243D
Nice to have
• Fb and insta icons. @velmiconstruct
Should not have
• No hammer or tool icons please.

No address line.

```html
<!DOCTYPE html>
<html lang="en">
<head>
<meta charset="utf-8">
<title>Velmi Construct – Business Card</title>
<link rel="stylesheet" href="https://fonts.googleapis.com/css2?family=Montserrat:wght@500;600&family=Work+Sans:wght@400;500&display=swap">
<style>
  :root {
    --stage-top: #353535;
    --stage-bottom: #0f0f0f;
    --brand-grey: #8c8c8c;
    --accent-grey: #7a7a7a;
    --card-white: #ffffff;
    --ink: #1e1e1e;
    --card-radius: 26px;
  }
  * { box-sizing: border-box; margin: 0; padding: 0; }
  html, body { width: 1200px; height: 900px; overflow: hidden; }
  body {
    background: radial-gradient(ellipse at 70% 10%, var(--stage-top), var(--stage-bottom) 75%);
    font-family: "Work Sans", sans-serif;
    position: relative;
  }
  .card {
    position: absolute;
    left: 290px;
    width: 620px;
    height: 370px;
    border-radius: var(--card-radius);
    box-shadow: 0 14px 30px rgba(0,0,0,0.55);
    overflow: hidden;
  }
  /* Front */
  .card--front {
    top: 50px;
    background: var(--brand-grey);
    display: flex;
    align-items: center;
    justify-content: center;
    gap: 22px;
  }
  .brand-square {
    width: 62px; height: 62px;
    border: 3px solid var(--card-white);
  }
  .brand-name {
    font-family: "Montserrat", sans-serif;
    font-weight: 500;
    font-size: 50px;
    letter-spacing: 16px;
    color: var(--card-white);
  }
  /* Back */
  .card--back { top: 470px; background: var(--card-white); }
  .company {
    position: absolute;
    left: 150px; top: 46px;
    font-family: "Montserrat", sans-serif;
  }
  .company__name {
    font-weight: 600;
    font-size: 32px;
    letter-spacing: 5px;
    color: var(--ink);
    line-height: 1;
  }
  .company__tagline {
    font-weight: 600;
    font-size: 17px;
    letter-spacing: 4.2px;
    color: var(--accent-grey);
    margin-top: 2px;
  }
  .details {
    position: absolute;
    left: 30px; right: 24px; top: 168px;
    display: flex;
    align-items: flex-start;
  }
  .person {
    width: 236px;
    text-align: right;
    flex: none;
  }
  .person__name {
    font-family: "Montserrat", sans-serif;
    font-weight: 600;
    font-size: 24px;
    letter-spacing: 1px;
    color: var(--accent-grey);
    line-height: 1.1;
    white-space: nowrap;
  }
  .person__role {
    font-size: 19px;
    letter-spacing: 1px;
    color: var(--ink);
    margin-top: 4px;
  }
  .divider {
    width: 2px; height: 50px;
    margin: 8px 14px 0 16px;
    background: var(--accent-grey);
    flex: none;
  }
  .contact {
    list-style: none;
    margin-top: 22px;
    font-size: 16px;
    letter-spacing: 0.5px;
    color: var(--ink);
    line-height: 1.4;
    white-space: nowrap;
  }
  .contact li { display: flex; align-items: center; gap: 6px; }
  .contact svg { width: 13px; height: 13px; flex: none; }
  .licence {
    position: absolute;
    left: 36px; bottom: 54px;
    font-size: 18px;
    letter-spacing: 1px;
    color: var(--ink);
  }
  .footer-rule {
    position: absolute;
    left: 240px; right: 112px; bottom: 52px;
    height: 1.5px;
    background: var(--accent-grey);
  }
  .social {
    position: absolute;
    right: 32px; bottom: 38px;
    display: flex; gap: 14px;
  }
  .social__tile {
    width: 30px; height: 30px;
    border-radius: 5px;
    background: var(--accent-grey);
  }
</style>
</head>
<body>
  <section class="card card--front" aria-label="Card front">
    <div class="brand-square"></div>
    <div class="brand-name">VELMI.</div>
  </section>

  <section class="card card--back" aria-label="Card back">
    <div class="company">
      <div class="company__name">VELMI CONSTRUCT</div>
      <div class="company__tagline">Carpentry &amp; Building Services</div>
    </div>

    <div class="details">
      <div class="person">
        <div class="person__name">NIKO BARLETTIS</div>
        <div class="person__role">Director</div>
      </div>
      <div class="divider"></div>
      <ul class="contact">
        <li>
          <svg viewBox="0 0 24 24" aria-hidden="true"><path fill="none" stroke="#7a7a7a" stroke-width="2.4" d="M6 3l3 4-2 2c1 3 4 6 7 7l2-2 4 3-2 4C10 21 3 14 2 5z"/></svg>
          0412385726
        </li>
        <li>
          <svg viewBox="0 0 24 24" aria-hidden="true"><rect x="2" y="5" width="20" height="14" fill="none" stroke="#7a7a7a" stroke-width="2.4"/><path d="M2 5l10 8 10-8" fill="none" stroke="#7a7a7a" stroke-width="2.4"/></svg>
          Velmiconstruct@brindlemail.com
        </li>
      </ul>
    </div>

    <div class="licence">Lic No. 618243D</div>
    <div class="footer-rule"></div>

    <div class="social" aria-label="Social links @velmiconstruct">
      <div class="social__tile"></div>
      <div class="social__tile"></div>
    </div>
  </section>
</body>
</html>
```